freshen up existing wordpress site

We wish to re-implement our current wordpress website www.vormalux.com/web2.

The content, structure and menus of the website should remain the same, but style updated to a more fresh/contemporary layout. It must be wordpress based and use a highly modifiable template like Bright Panels Kora or similar.

Permalinks must be exactly as the old ones.

Landing page must contain a slider for images and movies, plus a little text. There is no requirement for a tab-style as seem on the current website.

The final result shall be transferred to a fresh multisite installation of wordpress, we will provide login for access later. If another method is better/more preferred, please comment and we can take it from there.

The two graphics on http://vormalux.com/web2/gridmarshal-product-details/ should be re-done to look more 'clean and professional' and look less powerpoint'ish. We will need the vectorfiles for edits later on. Color scheme is open, whatever matches with the the website style.

We work in a engineering-heavy B2B environment, so slightly conservative/boring styles; no 'pop smartness'. competitors websites looks like this:
- http://www.halvorix.com/
- http://www.quernaly.com/
- https://www.brasketo.com/products/ic_nanometer_design/
- https://www.wolvane-da.com/

Website background should be white for easy image implementation. Our Vormalux logo colors can be used where applicable ( #1C62A6 #2454A0 #EF0315 #FB3A37 ), and matching or complementary colors too.

Use Sans Serif fonts like googles or something like http://www.glyphmarten.com/fonts/noto-sans .

Target Market(s)

semiconductor industry

Number of Pages Required

5+ page

Font styles to use
Sans Serif

Requirements
Must have
• see above
Nice to have
• see above
Should not have
• not defined.

```html
<!DOCTYPE html>
<html lang="en">
<head>
<meta charset="utf-8">
<title>Vormalux</title>
<link rel="stylesheet" href="https://fonts.googleapis.com/css2?family=Lato:wght@400;700;900&family=Raleway:wght@400;600;700&display=swap">
<style>
:root{
  --brand-blue:#1c62a6;
  --navy:#0f2a5c;
  --header-dark:#123a73;
  --red:#ef0315;
  --text:#222;
  --muted:#666;
  --field:#efefef;
  --field-line:#c9c9c9;
  --footer:#232323;
}
*{box-sizing:border-box;margin:0;padding:0}
html,body{width:1200px;height:945px;overflow:hidden;background:#fff}
body{position:relative;font-family:'Lato',sans-serif;color:var(--text)}
.topline{position:absolute;left:0;top:0;width:1200px;height:4px;background:var(--brand-blue)}
.site-header{position:absolute;left:0;top:4px;width:1200px;height:90px;border-bottom:4px solid var(--header-dark)}
.brand{position:absolute;left:131px;top:24px;display:flex;align-items:center;gap:10px}
.brand-mark{width:34px;height:34px;background:var(--brand-blue)}
.brand-name{font-family:'Lato',sans-serif;font-weight:900;font-size:40px;line-height:1;color:var(--navy);letter-spacing:-0.5px}
.phone{position:absolute;left:733px;top:6px;display:flex;align-items:center;gap:5px;font-weight:700;font-size:19px;color:#333}
.search{position:absolute;left:884px;top:0;width:183px;height:32px}
.search-label{position:absolute;left:29px;top:6px;color:#fff;font-size:13px;font-weight:700}
.main-nav{position:absolute;top:55px;left:594px;display:flex}
.main-nav a{font-size:14px;font-weight:700;color:var(--navy);text-decoration:none;margin-right:37px;letter-spacing:.2px}
.main-nav a.current{color:var(--brand-blue)}
.hero{position:absolute;left:0;top:98px;width:1200px;height:478px}
.hero-photo{position:absolute;top:0;height:478px}
.hero-photo.left{left:0;width:300px;background:linear-gradient(135deg,#1b4f9c,#2f7fd0 45%,#0e2c66)}
.hero-photo.center{left:300px;width:600px;background:linear-gradient(180deg,#121a22 0%,#2e3f35 50%,#5f7a2c 75%,#2c3a2a 100%)}
.hero-photo.right{left:900px;width:300px;background:linear-gradient(135deg,#b56a2a,#d98a3a 40%,#5a3a22)}
.hero-caption{position:absolute;left:352px;top:84px;width:424px;height:280px;background:rgba(10,12,14,.78);padding:28px 35px}
.hero-title{font-family:'Raleway',sans-serif;font-weight:400;font-size:39px;line-height:53px;color:#fff}
.hero-text{margin-top:20px;font-weight:700;font-size:17px;line-height:29px;color:#fff}
.hero-arrow{position:absolute;top:206px;width:38px;height:38px;border-radius:50%;background:#f3f3f3;box-shadow:0 2px 4px rgba(0,0,0,.4)}
.hero-arrow.prev{left:65px}.hero-arrow.next{left:1097px}
.hero-arrow svg{position:absolute;left:11px;top:11px}
.lower-band{position:absolute;left:0;top:576px;width:1200px;height:302px;background:linear-gradient(180deg,#e3e3e3,#fff 85%)}
.content-panel{position:absolute;left:130px;top:535px;width:938px;height:343px;background:#fff;box-shadow:0 0 12px rgba(0,0,0,.12)}
.column{position:absolute;top:18px}
.col-about{left:22px;width:262px}
.col-news{left:334px;width:263px}
.col-inquiry{left:650px;width:264px}
.divider{position:absolute;top:30px;width:1px;height:290px;background:#eee}
.section-title{font-family:'Raleway',sans-serif;font-weight:700;font-size:25px;line-height:30px;color:#111;padding:0 0 6px 2px;border-bottom:1px solid #ccc;position:relative}
.section-title span{color:var(--brand-blue)}
.section-title::after{content:"";position:absolute;left:0;bottom:-2px;width:94px;height:3px;background:var(--brand-blue)}
.about-photo{margin-top:15px;width:262px;height:133px;background:linear-gradient(90deg,#e8e8ea,#d8d4cf 60%,#b59a6c)}
.about-text{margin-top:8px;padding-left:2px;font-size:14px;line-height:21px;color:#333}
.read-more{position:absolute;display:flex;height:23px;font-size:13.5px;color:#fff;text-decoration:none}
.read-more .icon{width:23px;background:var(--brand-blue);display:flex;align-items:center;justify-content:center;margin-right:1px}
.read-more .label{background:var(--red);padding:0 7px;line-height:23px}
.news-list{list-style:none;margin-top:14px}
.news-item{display:flex;height:72px}
.news-date{width:49px;height:56px;flex:none;margin-left:2px;text-align:center;border-bottom:3px solid var(--brand-blue)}
.news-date .day{display:block;height:29px;background:var(--brand-blue);color:#fff;font-weight:700;font-size:19px;line-height:29px}
.news-date .month{display:block;background:#efefef;font-size:14px;line-height:24px;height:24px}
.news-body{margin-left:14px;width:200px}
.news-title{font-weight:700;font-size:14px;color:#222;line-height:16px;white-space:nowrap}
.news-excerpt{font-size:13px;color:var(--muted);line-height:19px;margin-top:3px}
.inquiry-form{margin-top:16px}
.field{display:block;width:262px;height:30px;margin:0 0 11px 2px;background:var(--field);border:1px solid var(--field-line);font-family:'Lato',sans-serif;font-size:13.5px;color:#555;padding:0 9px}
textarea.field{height:75px;padding-top:6px;resize:none}
.submit{margin-left:3px;width:81px;height:29px;border:0;background:var(--red);color:#fff;font-family:'Lato',sans-serif;font-weight:700;font-size:13.5px}
.site-footer{position:absolute;left:0;top:878px;width:1200px;height:67px;background:var(--footer);color:#fff}
.footer-nav{position:absolute;left:139px;top:26px;font-size:13px;font-weight:700}
.footer-nav a{color:#fff;text-decoration:none}
.footer-nav .sep{margin:0 11px}
.copyright{position:absolute;right:137px;top:26px;font-size:13.5px}
</style>
</head>
<body>
<div class="topline"></div>
<header class="site-header">
  <div class="brand"><span class="brand-mark"></span><span class="brand-name">Vormalux</span></div>
  <div class="phone">
    <svg width="16" height="18" viewBox="0 0 16 18"><path d="M3 1l3 0 1.5 4-2 1.5c1 2.5 2.5 4 5 5l1.5-2 4 1.5 0 3c0 1.5-1 2-2 2C7 16 1 10 1 3c0-1 .5-2 2-2z" fill="#ef3a37"/></svg>
    <span>123-456-7890</span>
  </div>
  <div class="search">
    <svg width="183" height="32" viewBox="0 0 183 32"><path d="M0 0H183L170 22Q162 32 150 32H30Q18 32 12 22Z" fill="#123a73"/></svg>
    <span class="search-label">Search Here</span>
    <svg style="position:absolute;left:133px;top:5px" width="20" height="20" viewBox="0 0 20 20"><circle cx="8" cy="8" r="6" fill="none" stroke="#fff" stroke-width="2"/><path d="M12.5 12.5L18 18" stroke="#fff" stroke-width="2.5"/></svg>
  </div>
  <nav class="main-nav">
    <a class="current" href="#">HOME</a><a href="#">PRODUCTS</a><a href="#">COMPANY</a><a href="#">NEWS</a><a href="#">CONTACT US</a>
  </nav>
</header>

<section class="hero">
  <div class="hero-photo left" role="img" aria-label="Close-up of a microchip on a blue circuit board"></div>
  <div class="hero-photo center" role="img" aria-label="Soldering tip over a green circuit board"></div>
  <div class="hero-photo right" role="img" aria-label="Soldering iron on an orange circuit board with chips"></div>
  <div class="hero-caption">
    <h1 class="hero-title">Grid Marshal<br>Adjustment</h1>
    <p class="hero-text">GridMarshal is different from a power rail analysis tool like Wolvane PeakFlow™, Halvorix Ampline™ or similar...</p>
  </div>
  <a class="hero-arrow prev" href="#" aria-label="Previous slide"><svg width="16" height="16" viewBox="0 0 16 16"><path d="M11 2L5 8l6 6" fill="none" stroke="#333" stroke-width="3"/></svg></a>
  <a class="hero-arrow next" href="#" aria-label="Next slide"><svg width="16" height="16" viewBox="0 0 16 16"><path d="M5 2l6 6-6 6" fill="none" stroke="#333" stroke-width="3"/></svg></a>
</section>

<div class="lower-band"></div>
<main class="content-panel">
  <section class="column col-about">
    <h2 class="section-title">About <span>Vormalux</span></h2>
    <div class="about-photo" role="img" aria-label="Gloved hand holding a processor chip"></div>
    <p class="about-text">Lorem ipsum dolor sit amet, consectetuer adipiscing elit, sed diam nonummy nibh euismod magna aliquam erat volutpat.</p>
  </section>
  <a class="read-more" href="#" style="left:24px;top:288px"><span class="icon"><svg width="11" height="8" viewBox="0 0 11 8"><path d="M0 4h9M6 1l3 3-3 3" fill="none" stroke="#fff"/></svg></span><span class="label">Read More</span></a>
  <div class="divider" style="left:309px"></div>

  <section class="column col-news">
    <h2 class="section-title">Latest <span>News</span></h2>
    <ul class="news-list">
      <li class="news-item"><div class="news-date"><span class="day">23</span><span class="month">JAN</span></div><div class="news-body"><h3 class="news-title">Lorem ipsum dolor sitak ametn</h3><p class="news-excerpt">Lorem ipsum dolor sitak amet, co adipiscing elit, euismod poor.</p></div></li>
      <li class="news-item"><div class="news-date"><span class="day">23</span><span class="month">JAN</span></div><div class="news-body"><h3 class="news-title">Lorem ipsum dolor sitak ametn</h3><p class="news-excerpt">Lorem ipsum dolor sitak amet, co adipiscing elit, euismod poor.</p></div></li>
      <li class="news-item"><div class="news-date"><span class="day">23</span><span class="month">JAN</span></div><div class="news-body"><h3 class="news-title">Lorem ipsum dolor sitak ametn</h3><p class="news-excerpt">Lorem ipsum dolor sitak amet, co adipiscing elit, euismod poor.</p></div></li>
    </ul>
  </section>
  <a class="read-more" href="#" style="left:337px;top:288px"><span class="icon"><svg width="11" height="8" viewBox="0 0 11 8"><path d="M0 4h9M6 1l3 3-3 3" fill="none" stroke="#fff"/></svg></span><span class="label">Read More</span></a>
  <div class="divider" style="left:623px"></div>

  <section class="column col-inquiry">
    <h2 class="section-title">Quick <span>Inquiry</span></h2>
    <form class="inquiry-form">
      <input class="field" type="text" placeholder="Name">
      <input class="field" type="email" placeholder="Email Address">
      <input class="field" type="tel" placeholder="Phone Number">
      <textarea class="field" placeholder="Message"></textarea>
      <button class="submit" type="button">SUBMIT</button>
    </form>
  </section>
</main>

<footer class="site-footer">
  <nav class="footer-nav"><a href="#">HOME</a><span class="sep">|</span><a href="#">PRODUCTS</a><span class="sep">|</span><a href="#">COMPANY</a><span class="sep">|</span><a href="#">NEWS</a><span class="sep">|</span><a href="#">CONTACT US</a></nav>
  <p class="copyright">Copyright © 2016&nbsp; Vormalux&nbsp; |&nbsp; All Right Reserved</p>
</footer>
</body>
</html>
```